BrivoLane Ute.

I want the full logo on one side. And the other side the card if right Ralf the logo the left half orange like the car in the logo color with Danielle R Morrow
Founder and CEO
Email symbol then dmorrow@brivolaneute.com
Www symbol. Then Brivolaneute.com
Phone symbol then 413-926-BRIV
The very bottom would like Brivo Lane Ute is a division of Harmond Vistas. LLC

```html
<!DOCTYPE html>
<html lang="en">
<head>
<meta charset="utf-8">
<title>Brivo Lane Ute — Business Card</title>
<link href="https://fonts.googleapis.com/css2?family=IM+Fell+English+SC&family=Lato:wght@400&family=Josefin+Sans:wght@400&display=swap" rel="stylesheet">
<style>
  :root {
    --backdrop: #252525;
    --paper: #ffffff;
    --paper-soft: #f7f7f5;
    --orange: #e68a23;
    --red: #e0312a;
    --ink: #1d1a17;
    --white: #ffffff;
  }
  * { margin: 0; padding: 0; box-sizing: border-box; }
  html, body {
    width: 979px; height: 1200px; overflow: hidden;
    background: var(--backdrop);
  }
  .canvas { position: relative; width: 979px; height: 1200px; }

  .card {
    position: absolute; left: 126px; width: 756px; height: 432px;
    border-radius: 29px; overflow: hidden; background: var(--paper);
  }
  .card--front { top: 102px; }
  .card--back { top: 642px; display: flex; }

  /* front */
  .brand-mark {
    position: absolute; left: 303px; top: 62px;
    width: 150px; height: 150px; border-radius: 50%;
    background: var(--orange);
  }
  .rule { position: absolute; height: 2px; background: var(--ink); }
  .front-rule--top { left: 106px; width: 548px; top: 234px; }
  .front-rule--bottom { left: 106px; width: 548px; top: 332px; }
  .brand-name {
    position: absolute; left: 0; right: 0; top: 244px;
    text-align: center;
    font-family: "IM Fell English SC", serif; font-weight: 400;
    font-size: 60px; line-height: 80px; color: var(--ink);
  }
  .tagline {
    position: absolute; left: 0; right: 0; top: 340px;
    text-align: center;
    font-family: "Josefin Sans", sans-serif;
    font-size: 18px; letter-spacing: 4px; color: var(--ink);
  }

  /* back */
  .contact-panel {
    position: relative; width: 378px; height: 100%;
    background: var(--orange); color: var(--white);
    text-align: center; font-family: "Lato", sans-serif;
  }
  .person-name {
    position: absolute; left: 0; right: 0; top: 56px;
    font-family: "IM Fell English SC", serif; font-weight: 400;
    font-size: 28px; color: var(--ink);
  }
  .person-title { position: absolute; left: 0; right: 0; top: 89px; font-size: 18px; }
  .panel-rule { left: 34px; width: 312px; }
  .panel-rule--top { top: 123px; }
  .panel-rule--bottom { top: 378px; }
  .contact-icons {
    position: absolute; left: 0; right: 0; top: 170px;
    display: flex; justify-content: center; gap: 10px;
  }
  .contact-icons svg { width: 16px; height: 16px; fill: var(--red); }
  .contact-list {
    position: absolute; left: 0; right: 0; top: 205px;
    list-style: none; font-size: 18px; line-height: 24.5px; letter-spacing: 0.5px;
  }
  .contact-list .accent { color: var(--red); }
  .division {
    position: absolute; left: 0; right: 0; top: 320px;
    font-size: 18px; line-height: 21px;
  }
  .division-brand {
    display: block; font-family: "IM Fell English SC", serif;
    font-size: 20px; color: var(--ink);
  }
  .logo-panel {
    position: relative; flex: 1; background: var(--paper-soft);
    display: flex; flex-direction: column; align-items: center; justify-content: center; gap: 12px;
  }
  .brand-mark--small {
    width: 64px; height: 64px; border-radius: 50%; background: var(--orange);
  }
  .brand-name--small {
    font-family: "IM Fell English SC", serif; font-size: 32px; color: var(--ink);
  }
</style>
</head>
<body>
<main class="canvas">
  <section class="card card--front" aria-label="Card front">
    <div class="brand-mark" aria-hidden="true"></div>
    <div class="rule front-rule--top"></div>
    <h1 class="brand-name">BRIVO LANE UTE</h1>
    <div class="rule front-rule--bottom"></div>
    <p class="tagline">DRIVE THE OPEN COAST</p>
  </section>

  <section class="card card--back" aria-label="Card back">
    <div class="contact-panel">
      <h2 class="person-name">DANIELLE R MORROW</h2>
      <p class="person-title">Founder and CEO</p>
      <div class="rule panel-rule panel-rule--top"></div>
      <div class="contact-icons" aria-hidden="true">
        <svg viewBox="0 0 24 24"><path d="M6.6 10.8a15.1 15.1 0 0 0 6.6 6.6l2.2-2.2a1 1 0 0 1 1-.25 11.4 11.4 0 0 0 3.6.57 1 1 0 0 1 1 1V20a1 1 0 0 1-1 1A17 17 0 0 1 3 4a1 1 0 0 1 1-1h3.5a1 1 0 0 1 1 1c0 1.25.2 2.45.57 3.57a1 1 0 0 1-.25 1z"/></svg>
        <svg viewBox="0 0 24 24"><path d="M2 5h20v2l-10 6L2 7z"/><path d="M2 9l10 6 10-6v10H2z"/></svg>
        <svg viewBox="0 0 24 24"><circle cx="12" cy="12" r="10"/><path d="M2 12h20M12 2c3 3 3 17 0 20M12 2c-3 3-3 17 0 20" stroke="#e68a23" stroke-width="1.5" fill="none"/></svg>
      </div>
      <ul class="contact-list">
        <li>413-926-BRIV</li>
        <li>dmorrow@<span class="accent">brivolaneute</span>.com</li>
        <li>www.<span class="accent">brivolaneute</span>.com</li>
      </ul>
      <p class="division"><span class="division-brand">Brivo Lane Ute</span>is a division of Harmond Vistas. LLC</p>
      <div class="rule panel-rule panel-rule--bottom"></div>
    </div>
    <div class="logo-panel">
      <div class="brand-mark--small" aria-hidden="true"></div>
      <p class="brand-name--small">Brivo Lane Ute</p>
    </div>
  </section>
</main>
</body>
</html>
```